Packaging Design - Labels for Organic Body Care Range

I am re-designing the current range of our Body Care Skin Care range.

It is a range of natural and organic skin care with 5 products.

The range is currently very girly and young look but we are opting for a more of a raw, edgy, organic look so that we will be well definited as being organic.

I am attaching the Design file of the the current packaging.

I have recently used Pixel Harbor to redesign our baby range and the beige background design was the one chosen:

http://www.pixelharbor-example.com/project-progress.aspx?briefId=58316&show=designs So something along these lines will be preferred so that it all goes together.

Have included some design inspiration below.

Look forward to seeing your designs.
Updates

I have updated the brief and included some design inspiration for these designs.

Hope this helps

Target Market(s)

Women 25 - 50 yrs

Industry/Entity Type

Baby

Requirements
Must have
• Natural feel
organic feel
Textured look
Eco chic
Luxury feel
Boutique feel
Nice to have
• bright colours
Sutble Floral (see example designs)
Should not have
• No minimilist designs ie Varnt, Thimb etc
No Purple, Blue, or green
Avoid too much pink

```html
<!DOCTYPE html>
<html lang="en">
<head>
<meta charset="utf-8">
<title>Kestrel Lane – Healing Hand &amp; Nail Cream Label</title>
<link rel="stylesheet" href="https://fonts.googleapis.com/css2?family=EB+Garamond:wght@400&family=Cormorant+SC:wght@500&family=Parisienne&display=swap">
<style>
  :root {
    --kraft: #c9a877;
    --kraft-light: #d6bb8e;
    --kraft-dark: #b8955f;
    --paper: #d9c6a3;
    --paper-light: #e3d3b4;
    --mist: #dfe4e3;
    --panel: rgba(245, 243, 236, 0.9);
    --frame: #9a9c98;
    --ink-grey: #8b8d89;
    --ink-body: #6e6a5f;
    --pink: #e08aa5;
    --petal: #ead0c0;
    --bloom: #f4efe6;
    --white: #ffffff;
  }
  * { box-sizing: border-box; margin: 0; padding: 0; }
  html, body { width: 1200px; height: 726px; overflow: hidden; background: var(--white); }
  .canvas { position: relative; width: 1200px; height: 726px; background: var(--white); }

  .brand-band {
    position: absolute; left: 0; top: 0; width: 1200px; height: 160px;
    background: linear-gradient(90deg, var(--kraft-light), var(--kraft) 45%, var(--kraft-light) 75%, var(--kraft));
    color: var(--white); font-family: "EB Garamond", serif;
  }
  .brand-band__name { position: absolute; left: 115px; top: 18px; font-size: 66px; font-weight: 400; line-height: 1; white-space: nowrap; }
  .brand-band__tagline { position: absolute; left: 117px; top: 108px; font-size: 33px; font-weight: 400; line-height: 1; white-space: nowrap; }

  .label { position: absolute; left: 108px; top: 240px; width: 552px; height: 432px; }

  .label__back {
    position: absolute; left: 0; top: 0; width: 217px; height: 432px;
    background: linear-gradient(180deg, var(--paper-light), var(--paper));
    color: var(--ink-body); text-align: center;
  }
  .cert-strip { position: absolute; left: 0; top: 0; width: 217px; height: 43px; background: var(--mist); display: flex; justify-content: center; gap: 24px; align-items: center; }
  .cert-badge { width: 24px; height: 24px; border-radius: 50%; border: 1px solid var(--white); }
  .back-copy { position: absolute; left: 30px; top: 68px; width: 157px; font-family: "Cormorant SC", serif; font-size: 8.4px; line-height: 9.6px; }
  .back-rule { position: absolute; left: 25px; top: 193px; width: 167px; border-top: 1.5px dotted var(--ink-body); }
  .ingredients-title { position: absolute; left: 0; top: 205px; width: 217px; font-family: "Cormorant SC", serif; font-size: 7px; }
  .ingredients { position: absolute; left: 18px; top: 220px; width: 181px; font-family: "EB Garamond", serif; font-size: 6px; line-height: 8.4px; opacity: .75; }
  .maker-strip { position: absolute; left: 0; bottom: 0; width: 217px; height: 42px; background: var(--mist); text-align: left; padding: 8px 10px; font-family: "EB Garamond", serif; font-size: 5px; line-height: 6.4px; color: var(--ink-grey); }

  .label__front {
    position: absolute; left: 217px; top: 0; width: 335px; height: 432px; overflow: hidden;
    background: linear-gradient(135deg, var(--kraft-dark), var(--kraft) 40%, var(--kraft-light) 70%, var(--kraft));
  }
  .art { position: absolute; }
  .art--bird { left: 100px; top: 28px; width: 72px; height: 68px; border-radius: 50% 40% 50% 40%; background: var(--bloom); opacity: .75; }
  .art--leaves { left: 0; top: 90px; width: 100px; height: 270px; border-radius: 60% 40% 40% 60%; background: linear-gradient(180deg, var(--petal), rgba(234,208,192,.4)); opacity: .8; }
  .art--flowers { left: 40px; top: 310px; width: 210px; height: 122px; border-radius: 50% 50% 0 0; background: radial-gradient(circle at 50% 60%, var(--bloom), rgba(244,239,230,.5)); opacity: .8; }
  .art--swirl { left: 270px; top: 160px; width: 65px; height: 110px; border-radius: 50% 0 50% 50%; background: var(--bloom); opacity: .75; }

  .front-panel {
    position: absolute; left: 75px; top: 105px; width: 205px; height: 203px;
    background: var(--panel); border: 2px solid var(--frame); text-align: center;
  }
  .front-panel__brand { margin-top: 10px; font-family: "EB Garamond", serif; font-size: 16px; line-height: 18px; color: var(--ink-grey); }
  .front-panel__product { margin-top: 20px; font-family: "Cormorant SC", serif; font-size: 13px; letter-spacing: .3px; color: var(--ink-grey); }
  .front-panel__claim { margin-top: 18px; font-family: "EB Garamond", serif; font-size: 13px; line-height: 13px; color: var(--pink); }
  .front-panel__scent { position: absolute; left: 0; bottom: 0; width: 100%; height: 32px; background: var(--mist); border-top: 1px solid var(--frame); font-family: "Parisienne", cursive; font-size: 19px; line-height: 32px; color: var(--ink-grey); white-space: nowrap; }
</style>
</head>
<body>
<main class="canvas">
  <header class="brand-band">
    <h1 class="brand-band__name">Kestrel Lane</h1>
    <p class="brand-band__tagline">Natural Organic Skin Care.</p>
  </header>

  <section class="label">
    <div class="label__back">
      <div class="cert-strip">
        <span class="cert-badge"></span><span class="cert-badge"></span><span class="cert-badge"></span>
      </div>
      <p class="back-copy">Nourish and heal dry hands, cuticles and feet with this heavenly hand and nail cream. Absorbs quickly and protects, nourishes and softens dry skin to promote healthy hands. It contains a certified organic blend of herbs and infused with organic shea butter and organic jojoba seed oil. Scented with a soothing blend of lavender, mandarin and chamomile essential oils.</p>
      <div class="back-rule"></div>
      <p class="ingredients-title">Ingredients</p>
      <p class="ingredients">Aqua, Aloe Leaf Juice, Shea Butter, Jojoba Seed Oil, Rosehip Oil, Sweet Almond Oil, Cetearyl Alcohol, Glycerin, Calendula Extract, Chamomile Extract, Lavender Oil, Mandarin Oil, Vitamin E, Cocoa Butter, Olive Oil, Sunflower Oil, Green Tea Extract, Rose Hydrosol, Oat Extract, Xanthan Gum, Citric Acid, Beeswax, Macadamia Oil, Apricot Kernel Oil, Avocado Oil, Evening Primrose Oil, Comfrey Extract, Marshmallow Root, Licorice Root, Honey, Grapeseed Oil, Coconut Oil, Borage Oil, Carrot Seed Oil, Sea Buckthorn, Plantain Extract, Geranium Oil, Vanilla Extract, Rice Bran Oil, Kakadu Plum, Lemon Myrtle, Native Mint.</p>
      <p class="maker-strip">Made in Australia<br>Kestrel Lane<br>www.kestrellane-example.com</p>
    </div>

    <div class="label__front">
      <div class="art art--leaves" role="img" aria-label="Pale pink leafy branch silhouettes"></div>
      <div class="art art--bird" role="img" aria-label="White hummingbird silhouette"></div>
      <div class="art art--swirl" role="img" aria-label="White curling petal flourish"></div>
      <div class="art art--flowers" role="img" aria-label="White peony and wildflower silhouettes"></div>

      <div class="front-panel">
        <p class="front-panel__brand">Kestrel Lane<br>Essentials</p>
        <p class="front-panel__product">Healing hand &amp; Nail cream</p>
        <p class="front-panel__claim">Contains an<br>organic herbal blend,<br>infused with organic shea butter,<br>rosehip oil &amp; jojoba seed oil</p>
        <p class="front-panel__scent">Lavender &amp; Mandarin</p>
      </div>
    </div>
  </section>
</main>
</body>
</html>
```